"Velvet Ember" sexual performance enhancement pill bottle label needed.

This should be interesting...

I am starting a line of sexual performance enhancement products. This will be the first of several products basically. Keep in mind, I am the type of business person to stay with one company for years if they provide me with quality work.

This particular product is a male sexual performance pill. The name of the product is "Velvet Ember." The packaging of the pills are a black bottle with a white top. Label on the product example would be perfect but at a minimum I have attached a "template" for your guidance.

Some of the technical aspects of this are as follows:

-File Format: Illustrator CS6 is preferred. (Winner must provide artwork in layer and can not flatten artwork.)
-Resolution: 300 dpi minimum
-Bleed: 1/16th (0.0625") inch from edge of label
-Color Mode: CMYK only or must be converted to CMYK for final production

Lastly, this is your project as a designer, artist, creator, this is essentially a piece of you that will be sold and known by thousands of people. I have no color scheme that I prefer, just use the template and follow the layout. If you have any further questions, please feel free to contact me at any time.
Updates

Quick note on the product and what it does: -Powerful, long lasting, harder erections -Works in a minutes and last for hours -Enhances sexual desire and drive Thank you for your ideas...

Project Deadline Extended
Reason: We decided to extent the project for a few more days to let the last few concepts come in. So far things are looking really good and we definitely have seen some amazing designs. Thank you for your hard work and amazing creativity. Looking forward to seeing what we have come in the next couple of day. Very respectfully, Doran

ONLY THREE DAYS LEFT!!!! Please submit your ideas as soon as possible. And as always, thank you for your help!!! V/r, Doran

Industry/Entity Type

Graphic Design

```html
<!DOCTYPE html>
<html lang="en">
<head>
<meta charset="utf-8">
<title>Velvet Ember – Bottle Label</title>
<link rel="stylesheet" href="https://fonts.googleapis.com/css2?family=Roboto+Condensed:wght@400;700&family=Macondo+Swash+Caps&display=swap">
<style>
  :root {
    --page-bg: #d9d9d9;
    --label-red: #e81b23;
    --label-dark: #0d0503;
    --ember: #f5b21b;
    --gold: #e9b536;
    --pill-red: #c4161c;
    --white: #ffffff;
  }
  html, body {
    margin: 0;
    width: 1022px;
    height: 1200px;
    overflow: hidden;
    background: var(--page-bg);
    font-family: "Roboto Condensed", "Arial Narrow", sans-serif;
  }
  .canvas {
    position: relative;
    width: 1022px;
    height: 1200px;
  }
  .label {
    position: absolute;
    left: 41px;
    top: 414px;
    width: 940px;
    height: 372px;
    border-radius: 16px;
    overflow: hidden;
    color: var(--white);
    background:
      radial-gradient(ellipse 300px 260px at 50% 55%, rgba(13,5,3,1) 40%, rgba(13,5,3,0) 100%),
      linear-gradient(90deg, var(--label-red) 0%, var(--label-red) 24%, #5a0b08 32%, var(--label-dark) 40%, var(--label-dark) 60%, #5a0b08 68%, var(--label-red) 76%, var(--label-red) 100%);
    box-shadow: 0 4px 10px rgba(0,0,0,.35);
  }

  /* left column */
  .directions {
    position: absolute;
    left: 28px;
    top: 40px;
    width: 202px;
    font-size: 7.6px;
    line-height: 1.28;
    text-align: justify;
  }
  .directions p { margin: 0 0 6px; }
  .directions .storage { margin-top: 12px; }
  .fda-note {
    position: absolute;
    left: 28px;
    top: 228px;
    width: 194px;
    padding: 3px 4px;
    border: 1.5px solid var(--white);
    font-size: 7.4px;
    line-height: 1.25;
  }
  .maker {
    position: absolute;
    left: 32px;
    top: 284px;
    font-size: 11px;
    line-height: 1.3;
  }

  /* centre panel */
  .badge {
    position: absolute;
    left: 278px;
    top: 70px;
    width: 56px;
    height: 56px;
    border-radius: 50%;
    background: #e6731a;
    border: 3px solid var(--gold);
    box-sizing: border-box;
  }
  .tagline {
    position: absolute;
    left: 300px;
    width: 340px;
    top: 68px;
    margin: 0;
    text-align: center;
    font-family: "Macondo Swash Caps", cursive;
    font-size: 13px;
    line-height: 18px;
    color: var(--ember);
    letter-spacing: .3px;
  }
  .rule-gold {
    position: absolute;
    left: 338px;
    width: 268px;
    height: 3px;
    background: linear-gradient(90deg, rgba(233,181,54,0), var(--gold) 15%, #fff0a8 50%, var(--gold) 85%, rgba(233,181,54,0));
  }
  .rule-gold.top { top: 100px; }
  .rule-gold.bottom { top: 166px; }
  .product-name {
    position: absolute;
    left: 300px;
    width: 340px;
    top: 108px;
    height: 54px;
    margin: 0;
    text-align: center;
    font-size: 46px;
    font-weight: 700;
    line-height: 54px;
    color: var(--white);
    letter-spacing: .5px;
  }
  .ember-burst {
    position: absolute;
    left: 262px;
    top: 176px;
    width: 416px;
    height: 124px;
    background: radial-gradient(ellipse 200px 60px at 50% 50%, rgba(255,236,150,.95) 0%, rgba(245,150,30,.7) 18%, rgba(200,70,20,.35) 45%, rgba(13,5,3,0) 100%);
  }
  .claim {
    position: absolute;
    left: 334px;
    top: 228px;
    width: 274px;
    height: 22px;
    border-radius: 11px;
    background: var(--pill-red);
    border: 2px solid var(--gold);
    box-sizing: border-box;
    text-align: center;
    font-size: 12px;
    line-height: 18px;
    color: #ffe98a;
    letter-spacing: .2px;
  }
  .promise {
    position: absolute;
    left: 343px;
    top: 306px;
    font-size: 13.5px;
    line-height: 17px;
  }
  .count {
    position: absolute;
    left: 462px;
    top: 312px;
    font-size: 13px;
  }
  .count b { font-size: 22px; font-weight: 700; }

  /* right column */
  .facts {
    position: absolute;
    left: 722px;
    top: 56px;
    width: 198px;
    font-size: 9px;
    line-height: 1.3;
  }
  .facts h2 {
    margin: 0 0 4px;
    font-size: 24px;
    font-weight: 400;
    letter-spacing: -.2px;
  }
  .facts .serving { font-weight: 700; font-size: 10px; }
  .facts hr {
    border: 0;
    border-top: 1.5px solid var(--white);
    margin: 4px 0;
  }
  .facts .row {
    display: flex;
    justify-content: space-between;
    font-weight: 700;
  }
  .facts .blend { text-align: justify; }
  .facts .other { margin-top: 16px; font-size: 8px; }
</style>
</head>
<body>
<main class="canvas">
  <section class="label">

    <div class="directions">
      <p>SUGGESTED USE: As a dietary supplement, take two (2) capsules 1 hour before physical activity, or as directed by your health care professional. Do not exceed two (2) capsules daily.</p>
      <p>CAUTION: Do not exceed recommended dose. This product is not intended for pregnant or nursing mothers, children under the age of 18, or individuals taking prescription drugs. Discontinue use immediately if nausea, sleeplessness, or nervousness occur. Do not take this product if you have a known medical condition including high blood pressure, diabetes, any cardiovascular disorder, heart disease, hyperthyroidism, or are taking anti-depressant medications. If you have questions about the advisability of taking this product, consult your physician prior to use.</p>
      <p class="storage">KEEP OUT OF THE REACH OF CHILDREN. DO NOT USE IF SAFETY SEAL IS DAMAGED OR MISSING. STORE AT ROOM TEMPERATURE.</p>
    </div>

    <div class="fda-note">* These statements have not been evaluated by the Food and Drug Administration. This product is not intended to diagnose, treat, cure or prevent any disease.</div>

    <div class="maker">Manufactured Exclusively For:<br>COMPANY INFO</div>

    <div class="badge" role="img" aria-label="Guarantee seal"></div>
    <p class="tagline">Enhances Sexual Desire and Drive</p>
    <div class="rule-gold top"></div>
    <h1 class="product-name">VELVET EMBER</h1>
    <div class="rule-gold bottom"></div>
    <div class="ember-burst" role="img" aria-label="Glowing starburst with scattered golden sparks"></div>
    <div class="claim">POWERFUL, LONG LASTING, HARDER ERECTIONS</div>
    <div class="promise">Works in a minutes<br>and last for hours</div>
    <div class="count"><b>60</b>Pills</div>

    <div class="facts">
      <h2>Supplement Facts</h2>
      <div class="serving">Serving Size: 2 Capsules<br>Servings Per Container: 30</div>
      <hr>
      <div class="row"><span>Amount Per Serving</span><span>% Daily Value</span></div>
      <hr>
      <div class="row"><span>VE-Rx™ Proprietary Formula</span><span>1,560 mg &nbsp;†</span></div>
      <div class="blend">Horny Goat Weed (herb powder), Maca (herb powder), Macuna Pruriens (L-Dopa), Polypodium Vulgare (herb powder), Yohimbe Bark (herb powder), Saw Palmetto (herb powder), Muira Puama (herb powder), Arginine (L-Arginine hydrochloride), Panax Ginseng (herb powder)</div>
      <hr>
      <div>† % Daily Value not established</div>
      <div class="other">Other Ingredients: Gelatin, Magnesium Stearate, and Calcium Carbonate.</div>
    </div>

  </section>
</main>
</body>
</html>
```